Mt Corrabin - Outback Australia (Working farm, film location and farmstay promotation)

I need a website to promote my film location and farm stay business. Would like the ability to have online booking also and payment options

REFER TO
https://rs.sitevaultex.example/location_detail.aspx?id=418-55291346&search=broken%20hill&search_mode=and&ctry=all&state=&city=&cat=&subcat=&style=&lname=&locid=&int=&parent=search_results

https://www.facebook.example/pg/mountcorrabinstation/photos/?ref=page_internal

Target Market(s)

International Tourists
Film crews

Coding

Coded - Design and coding required

Number of Pages Required

1 page

Colors

Designer to choose colors to be used in the design.

Requirements
Must have
• Ability for online booking

```html
<!DOCTYPE html>
<html lang="en">
<head>
<meta charset="utf-8">
<title>Mt Corrabin Station</title>
<link href="https://fonts.googleapis.com/css2?family=Poppins:wght@300;400;500;600;700&display=swap" rel="stylesheet">
<style>
:root{
  --orange:#f26a10;
  --orange-dark:#d95800;
  --ink:#222222;
  --muted:#6f6f6f;
  --line:#e3e3e3;
  --panel:#f5f5f5;
  --footer:#1b1b1b;
  --white:#ffffff;
}
*{box-sizing:border-box;margin:0;padding:0}
html,body{width:1200px;height:3188px;overflow:hidden}
body{font-family:'Poppins',sans-serif;color:var(--ink);background:var(--white);position:relative}
a{color:inherit;text-decoration:none}
.abs{position:absolute}
.btn{display:inline-block;background:var(--orange);color:var(--white);border-radius:20px;font-size:13px;font-weight:600;padding:8px 26px}
.btn-outline{display:inline-block;border:1px solid var(--orange);color:var(--ink);border-radius:20px;font-size:13px;font-weight:500;padding:7px 26px;background:var(--white)}
.accent{color:var(--orange)}

/* header */
.site-header{position:absolute;left:0;top:0;width:1200px;height:112px;background:var(--white);z-index:3}
.brand{position:absolute;left:85px;top:22px;display:flex;align-items:center;gap:10px}
.brand-dot{width:34px;height:34px;border-radius:50%;background:var(--orange)}
.brand-name{font-size:24px;font-weight:700;color:var(--orange);line-height:1}
.topbar{position:absolute;right:90px;top:28px;display:flex;align-items:center;gap:22px;font-size:13px}
.topbar .call{color:var(--orange);font-weight:500}
.nav{position:absolute;right:90px;top:70px;display:flex;gap:52px;font-size:13px;font-weight:500}
.nav a.active{color:var(--orange)}

/* hero */
.hero{position:absolute;left:0;top:100px;width:1200px;height:530px;
  background:linear-gradient(180deg,#bcc6cc 0%,#9aa0a0 35%,#7d6a58 62%,#8a5a3a 100%)}
.hero-text{position:absolute;left:85px;top:150px;width:420px;color:var(--white);font-size:28px;line-height:1.28;font-weight:300}
.hero-text strong{font-weight:700}
.hero-text .accent{font-weight:600}
.hero .find{position:absolute;left:85px;top:268px;border:1px solid var(--white);color:var(--white);font-size:12px;padding:5px 16px;border-radius:16px}
.hero-curve{position:absolute;left:0;top:520px;width:1200px;height:130px}

/* about */
.about{position:absolute;left:0;top:650px;width:1200px;text-align:center}
.section-title{font-size:30px;font-weight:500;text-align:center}
.about p{width:560px;margin:20px auto 24px;font-size:14px;line-height:1.6}
.about p strong{font-weight:600}

/* services */
.services{position:absolute;left:0;top:890px;width:1200px;height:570px;background:var(--white)}
.services-rule{position:absolute;left:0;top:0;width:1200px;height:1px;background:var(--line)}
.services .section-title{position:absolute;top:72px;width:1200px}
.service{position:absolute;top:150px;width:300px;text-align:center}
.service-photo{width:160px;height:160px;border-radius:50%;margin:0 auto;position:relative}
.service-swoosh{position:absolute;left:-20px;top:140px;width:200px;height:40px}
.service-badge{position:absolute;left:60px;top:135px;width:40px;height:40px;border-radius:50%;background:var(--orange);display:flex;align-items:center;justify-content:center}
.service h3{margin-top:40px;font-size:17px;font-weight:600}
.service p{margin-top:8px;font-size:12px;color:var(--muted);line-height:1.5;padding:0 30px}

/* booking */
.booking{position:absolute;left:85px;top:1370px;width:495px;height:300px;background:var(--panel);border-radius:4px;padding:26px 28px}
.booking h2{font-size:22px;font-weight:500}
.booking .sub{font-size:11px;color:var(--muted);margin-top:2px}
.field-grid{display:grid;grid-template-columns:1fr 1fr;gap:14px;margin-top:22px}
.field{background:var(--white);border:1px solid var(--line);height:34px;border-radius:3px;font-size:11px;color:#999;padding:9px 12px}
.booking .submit{margin-top:16px;width:100%;height:34px;background:var(--orange);color:var(--white);border-radius:18px;font-size:12px;font-weight:600;text-align:center;line-height:34px}

.weather{position:absolute;left:640px;top:1385px;width:470px;height:275px;border:1px solid var(--line);border-radius:4px;padding:18px 22px}
.weather-head{display:flex;justify-content:space-between;font-size:12px;font-weight:600}
.weather-head span{font-weight:400;color:var(--muted);font-size:11px}
.weather-now{position:absolute;left:22px;top:60px;width:140px}
.weather-now .temp{font-size:44px;font-weight:500;line-height:1;padding-left:36px}
.weather-now .desc{font-size:11px;color:var(--muted);padding-left:40px;margin-top:4px}
.weather-now .label{font-size:12px;font-weight:600;padding-left:40px;margin-top:14px}
.weather-days{position:absolute;left:175px;top:56px;display:flex;gap:12px}
.day{width:22px;text-align:center;font-size:10px;color:var(--muted)}
.day .bar{margin:8px auto 0;width:10px;background:#3a3a3a;border-radius:5px}

/* gallery */
.gallery{position:absolute;left:0;top:1740px;width:1200px}
.gallery .section-title span{color:var(--orange)}
.tile{position:absolute}
.load-more{position:absolute;left:540px;top:2325px}

/* footer */
.footer{position:absolute;left:0;top:2400px;width:1200px;height:788px;background:var(--footer);color:var(--white)}
.footer-curve{position:absolute;left:0;top:-1px;width:1200px;height:80px}
.footer .edge{position:absolute;left:0;top:0;width:1200px;height:6px}
.contact{position:absolute;left:85px;top:200px;width:380px}
.contact h2{font-size:26px;font-weight:500}
.contact .addr{margin-top:26px;font-size:12px;line-height:1.6;color:#d8d8d8}
.contact .phone{margin-top:10px;font-size:13px;color:var(--orange);font-weight:600}
.contact .mail{font-size:12px;color:#d8d8d8;margin-top:4px}
.contact .btn{margin-top:22px}
.social{display:flex;gap:10px;margin-top:22px}
.social i{display:block;width:28px;height:28px;border-radius:50%;background:var(--orange)}
.map{position:absolute;left:530px;top:200px;width:580px;height:215px;background:linear-gradient(135deg,#e9e9e6,#d9dcd6)}
.disclaimer{position:absolute;left:85px;top:578px;width:1025px;font-size:11px;line-height:1.55;color:#b0b0b0}
.disclaimer strong{color:var(--orange);font-weight:600}
.footer-rule{position:absolute;left:85px;top:708px;width:1025px;height:1px;background:#3a3a3a}
.copyright{position:absolute;left:85px;top:722px;font-size:11px;color:#9a9a9a}
.to-top{position:absolute;left:1088px;top:718px}
</style>
</head>
<body>

<header class="site-header">
  <a class="brand" href="#home"><span class="brand-dot"></span><span class="brand-name">Mt Corrabin</span></a>
  <div class="topbar">
    <span class="call">Call us : +61 2 5550 1274</span>
    <a class="btn" href="#book">Book Now</a>
  </div>
  <nav class="nav">
    <a class="active" href="#home">Home</a>
    <a href="#about">About Us</a>
    <a href="#services">Services</a>
    <a href="#gallery">Gallery</a>
    <a href="#location">Location</a>
    <a href="#contact">Contact us</a>
  </nav>
</header>

<section class="hero" id="home" role="img" aria-label="Outback homestead with a long verandah under a pale sky on red earth">
  <p class="hero-text">Contrary to <span class="accent">Popular work</span> Belief, Lorem Ipsum classical <strong>randomised</strong> words!</p>
  <a class="find" href="#about">Find Out</a>
</section>
<svg class="hero-curve" viewBox="0 0 1200 130" preserveAspectRatio="none" aria-hidden="true">
  <path d="M0 0 Q600 150 1200 0 L1200 130 L0 130 Z" fill="#ffffff"/>
</svg>

<section class="about" id="about">
  <h2 class="section-title">About <span class="accent">Mt Corrabin</span></h2>
  <p><strong>Mt Corrabin Station is an 85,000 acre sheep</strong> and cattle property about 40km/30 minute drive north of the regional city on Hill. Features include hills, gorges, mines, rock formations and creeks.</p>
  <a class="btn-outline" href="#about">Read more</a>
</section>

<section class="services" id="services">
  <div class="services-rule"></div>
  <h2 class="section-title">Our <span class="accent">Services</span></h2>

  <div class="service" style="left:150px">
    <div class="service-photo" role="img" aria-label="Homestead bedroom interior" style="background:radial-gradient(circle at 40% 40%,#d8c6a8,#8e6f4e)">
      <svg class="service-swoosh" viewBox="0 0 200 40" aria-hidden="true"><path d="M0 10 Q100 50 200 10" stroke="#222" stroke-width="4" fill="none"/></svg>
      <div class="service-badge"><svg width="20" height="16" viewBox="0 0 20 16"><rect x="1" y="6" width="18" height="7" fill="#fff"/><rect x="3" y="3" width="6" height="4" fill="#fff"/><rect x="1" y="13" width="2" height="3" fill="#fff"/><rect x="17" y="13" width="2" height="3" fill="#fff"/></svg></div>
    </div>
    <h3>Accommodation</h3>
    <p>Lorem Ipsum is simply dummy text of printing and typesetting industry. Lorem Ipsum has been industry's standard.</p>
  </div>

  <div class="service" style="left:450px">
    <div class="service-photo" role="img" aria-label="Table set with a shared meal" style="background:radial-gradient(circle at 50% 40%,#e6d2c0,#9c3a2e)">
      <svg class="service-swoosh" viewBox="0 0 200 40" aria-hidden="true"><path d="M0 10 Q100 50 200 10" stroke="#222" stroke-width="4" fill="none"/></svg>
      <div class="service-badge"><svg width="16" height="18" viewBox="0 0 16 18"><path d="M3 1v6M1 1v4a2 2 0 004 0V1M3 7v10M12 1c-2 2-2 6 0 7v9" stroke="#fff" stroke-width="1.6" fill="none"/></svg></div>
    </div>
    <h3>Dining</h3>
    <p>Lorem Ipsum is simply dummy text of printing and typesetting industry. Lorem Ipsum has been industry's standard.</p>
  </div>

  <div class="service" style="left:750px">
    <div class="service-photo" role="img" aria-label="Campfire at dusk" style="background:radial-gradient(circle at 50% 65%,#e07a2a,#2a2320 70%)">
      <svg class="service-swoosh" viewBox="0 0 200 40" aria-hidden="true"><path d="M0 10 Q100 50 200 10" stroke="#222" stroke-width="4" fill="none"/></svg>
      <div class="service-badge"><svg width="20" height="16" viewBox="0 0 20 16"><path d="M1 15L10 2l9 13Z" fill="#fff"/><path d="M8 15l2-4 2 4Z" fill="#f26a10"/></svg></div>
    </div>
    <h3>Caravan and Camp</h3>
    <p>Lorem Ipsum is simply dummy text of printing and typesetting industry. Lorem Ipsum has been industry's standard.</p>
  </div>
</section>

<section class="booking" id="book">
  <h2>Check <span class="accent">Available Dates</span></h2>
  <p class="sub">Please choose an arrival and departure date</p>
  <div class="field-grid">
    <div class="field">Arrival Date</div>
    <div class="field">Departure Date</div>
    <div class="field">Adults</div>
    <div class="field">Children</div>
  </div>
  <div class="submit">Check availability</div>
</section>

<aside class="weather">
  <div class="weather-head">Weather for Dry Creek <span>More 7-day fc</span></div>
  <div class="weather-now">
    <svg class="abs" style="left:0;top:4px" width="30" height="30" viewBox="0 0 30 30"><path d="M24 8A11 11 0 1 0 24 22" stroke="#222" stroke-width="4" fill="none"/></svg>
    <div class="temp">25°</div>
    <div class="desc">Sun Rising</div>
    <div class="label">Clear</div>
    <div class="desc" style="margin-top:0">Wind: 5km/h south</div>
  </div>
  <div class="weather-days">
    <div class="day">Today<div class="bar" style="height:40px"></div></div>
    <div class="day">Sat<div class="bar" style="height:48px"></div></div>
    <div class="day">Sun<div class="bar" style="height:36px"></div></div>
    <div class="day">Thu<div class="bar" style="height:44px"></div></div>
    <div class="day">Fri<div class="bar" style="height:38px"></div></div>
    <div class="day">Sat<div class="bar" style="height:50px"></div></div>
    <div class="day">Sun<div class="bar" style="height:42px"></div></div>
    <div class="day">Mon<div class="bar" style="height:46px"></div></div>
  </div>
</aside>

<section class="gallery" id="gallery">
  <h2 class="section-title">Photo <span>Gallery</span></h2>
</section>
<div class="tile" style="left:85px;top:1812px;width:425px;height:228px;background:linear-gradient(180deg,#c9cfd1,#8b8e7a 55%,#6c7458)" role="img" aria-label="Homestead with agave plants in the garden"></div>
<div class="tile" style="left:530px;top:1812px;width:230px;height:228px;background:linear-gradient(180deg,#c6ccd2,#a39a86 60%,#8c6a4a)" role="img" aria-label="Stone cottage on open plain"></div>
<div class="tile" style="left:780px;top:1812px;width:330px;height:228px;background:linear-gradient(180deg,#cfd3d6,#9e8b76 60%,#8a5b3c)" role="img" aria-label="Shearing sheds and yards"></div>
<div class="tile" style="left:85px;top:2058px;width:225px;height:232px;background:linear-gradient(180deg,#c2c9cf,#9a8576 55%,#6b5446)" role="img" aria-label="Rocky outcrop in the hills"></div>
<div class="tile" style="left:330px;top:2058px;width:230px;height:232px;background:linear-gradient(180deg,#d6772f,#b9561e)" role="img" aria-label="Red dirt track, more photos">
  <svg class="abs" style="left:105px;top:106px" width="20" height="20" viewBox="0 0 20 20"><path d="M10 0v20M0 10h20" stroke="#fff" stroke-width="2"/></svg>
</div>
<div class="tile" style="left:580px;top:2058px;width:530px;height:232px;background:linear-gradient(180deg,#c8ced3,#a49a86 55%,#8d6a48)" role="img" aria-label="Homestead and outbuildings beneath a wide sky"></div>
<a class="btn-outline load-more" href="#gallery">Load More</a>

<footer class="footer" id="contact">
  <svg class="footer-curve" viewBox="0 0 1200 80" preserveAspectRatio="none" aria-hidden="true">
    <path d="M0 0 L1200 0 L1200 20 Q600 110 0 20 Z" fill="#ffffff"/>
    <path d="M0 20 Q600 110 1200 20" stroke="#f26a10" stroke-width="3" fill="none"/>
  </svg>

  <div class="contact">
    <h2>Contact <span class="accent">Us</span></h2>
    <p class="addr">Mount Corrabin Station<br>Dry Creek, NSW 2899</p>
    <p class="phone">CALL: +61 2 5550 1274</p>
    <p class="mail">E: info@mountcorrabinstation.example</p>
    <a class="btn" href="#book">Book Now</a>
    <div class="social"><i></i><i></i></div>
  </div>

  <div class="map" id="location" role="img" aria-label="Map showing the station location">
    <svg class="abs" style="left:150px;top:88px" width="22" height="30" viewBox="0 0 22 30"><path d="M11 0a11 11 0 0 0-11 11c0 8 11 19 11 19s11-11 11-19A11 11 0 0 0 11 0z" fill="#e0241b"/><circle cx="11" cy="11" r="4" fill="#fff"/></svg>
  </div>

  <p class="disclaimer"><strong>Disclaimer:</strong> All data, information and maps are provided "as is" without warranty or any representation of accuracy, timeliness or completeness. The content on this site is offered as a guide only and may change without notice. Visitors should confirm access, road conditions and bookings directly with the station before travelling. The owners accept no liability for any loss or damage arising from use of this information, and guests remain responsible for their own safety at all times on a working property.</p>
  <div class="footer-rule"></div>
  <p class="copyright">© 2024 Mount Corrabin Station. All Rights Reserved.</p>
  <svg class="to-top" width="22" height="22" viewBox="0 0 22 22" aria-label="Back to top"><path d="M4 16L11 6l7 10Z" fill="#f26a10"/></svg>
</footer>

</body>
</html>
```